Real Estate Managemene Company Needs Business Card Design

We have a logo design and just need business cards made now for our business. Please use PDF logo # 3.

Card with Information to be attached shortly.

The card is used for a real estate management company. We will need to add four other employees and their cards.

Industry/Entity Type

Real Estate

Contact Information for Business Card

Tariq Hamdan
President
3187 Thornwick Avenue
Suite C
Glendale Heights, IL 60152
Phone 630.417.2286
Fax 630.417.2287
Cell 630.473.8062
vantorp@mailbreeze.net

Once design is approved we will have four other employees
Omar Hamdan
Operations Manager

Nadia Hamdan
Administrative Manager

Faz Hamdan
Principal

We would need to take out the cell # 630.473.8062 out for the remaining three cards.

Requirements
Must have
• Please use logo attached

```html
<!DOCTYPE html>
<html lang="en">
<head>
<meta charset="utf-8">
<title>Meridian Property Management Group – Business Card</title>
<link rel="stylesheet" href="https://fonts.googleapis.com/css2?family=Oswald:wght@300;400&family=Pathway+Gothic+One&display=swap">
<style>
  :root {
    --backdrop: #e6e6e6;
    --charcoal: #2a2829;
    --brand-blue: #0b5c96;
    --white: #ffffff;
    --title-dark: #23272b;
  }
  * { margin: 0; padding: 0; box-sizing: border-box; }
  html, body {
    width: 1200px;
    height: 813px;
    overflow: hidden;
    background: var(--backdrop);
  }
  .card {
    position: absolute;
    left: 180px;
    top: 166px;
    width: 840px;
    height: 480px;
    display: flex;
    box-shadow: 0 12px 30px rgba(0, 0, 0, 0.18);
  }
  .card__company {
    width: 475px;
    background: var(--charcoal);
    color: var(--white);
    position: relative;
  }
  .brand {
    position: absolute;
    left: 70px;
    top: 78px;
    display: flex;
    align-items: center;
    gap: 16px;
  }
  .brand__mark {
    width: 22px;
    height: 22px;
    background: var(--brand-blue);
    flex: none;
  }
  .brand__name {
    font-family: "Oswald", sans-serif;
    font-weight: 400;
    font-size: 30px;
    line-height: 1.15;
    letter-spacing: 2px;
    text-transform: uppercase;
    color: var(--white);
  }
  .address {
    position: absolute;
    right: 36px;
    top: 262px;
    text-align: right;
    font-family: "Pathway Gothic One", sans-serif;
    font-style: normal;
    font-size: 30px;
    line-height: 1.3;
    color: var(--white);
  }
  .card__person {
    flex: 1;
    background: var(--brand-blue);
    color: var(--white);
    padding: 44px 0 0 30px;
  }
  .person__name {
    font-family: "Oswald", sans-serif;
    font-weight: 300;
    font-size: 54px;
    line-height: 1;
    white-space: nowrap;
    text-transform: uppercase;
  }
  .person__title {
    font-family: "Pathway Gothic One", sans-serif;
    font-size: 24px;
    letter-spacing: 1px;
    color: var(--title-dark);
    text-transform: uppercase;
    margin-top: 4px;
  }
  .contacts {
    list-style: none;
    margin-top: 40px;
  }
  .contacts__item {
    display: flex;
    align-items: center;
    gap: 14px;
    height: 48px;
    font-family: "Pathway Gothic One", sans-serif;
    font-size: 29px;
  }
  .contacts__icon {
    width: 32px;
    height: 32px;
    flex: none;
  }
</style>
</head>
<body>
  <article class="card">
    <section class="card__company">
      <div class="brand">
        <span class="brand__mark"></span>
        <p class="brand__name">Meridian Property<br>Management Group</p>
      </div>
      <address class="address">
        3187 Thornwick Avenue<br>
        Suite C<br>
        Brookhaven Falls, OR 97418
      </address>
    </section>

    <section class="card__person">
      <h1 class="person__name">Tariq Hamdan</h1>
      <p class="person__title">President</p>
      <ul class="contacts">
        <li class="contacts__item">
          <svg class="contacts__icon" viewBox="0 0 32 32" aria-hidden="true">
            <circle cx="16" cy="16" r="16" fill="#ffffff"/>
            <path d="M11 8.5c1-.6 2-.3 2.4.6l1.2 2.6c.3.7.1 1.4-.5 1.9l-1 .8c.8 1.8 2.2 3.3 4 4.2l.9-1c.5-.6 1.3-.7 1.900-.4l2.5 1.3c.9.4 1.1 1.5.5 2.4l-.9 1.2c-.8 1-2.2 1.3-3.4.8-4.2-1.8-7.3-5-8.900-9.2-.4-1.2 0-2.5 1.1-3.2z" fill="#0b5c96"/>
          </svg>
          <span>555.417.2286</span>
        </li>
        <li class="contacts__item">
          <svg class="contacts__icon" viewBox="0 0 32 32" aria-hidden="true">
            <circle cx="16" cy="16" r="16" fill="#ffffff"/>
            <rect x="11" y="7" width="10" height="6" fill="#0b5c96"/>
            <rect x="8" y="12" width="16" height="11" rx="1.5" fill="#0b5c96"/>
            <rect x="11" y="15" width="10" height="1.6" fill="#ffffff"/>
            <rect x="11" y="18.5" width="10" height="1.6" fill="#ffffff"/>
            <rect x="10" y="23" width="12" height="2.5" fill="#0b5c96"/>
          </svg>
          <span>555.417.2287</span>
        </li>
        <li class="contacts__item">
          <svg class="contacts__icon" viewBox="0 0 32 32" aria-hidden="true">
            <circle cx="16" cy="16" r="16" fill="#ffffff"/>
            <rect x="11" y="7" width="10" height="18" rx="2" fill="#0b5c96"/>
            <rect x="12.5" y="9.5" width="7" height="11" fill="#ffffff"/>
            <circle cx="16" cy="22.7" r="1" fill="#ffffff"/>
          </svg>
          <span>Cell 555.473.8062</span>
        </li>
        <li class="contacts__item">
          <svg class="contacts__icon" viewBox="0 0 32 32" aria-hidden="true">
            <circle cx="16" cy="16" r="16" fill="#ffffff"/>
            <rect x="8" y="10" width="16" height="12" rx="1" fill="#0b5c96"/>
            <path d="M8.5 10.5 16 17l7.5-6.5" fill="none" stroke="#ffffff" stroke-width="1.5"/>
          </svg>
          <span>vantorp@mailbreeze.net</span>
        </li>
      </ul>
    </section>
  </article>
</body>
</html>
```